Business Advisory Firm Business Card

A clean, very upscale looking business card. Not crowded.

Please include logo (attached) and:

Danielle R. Kastrup
Four Ashgrove Court
New York, NY 10087
tel: (917) 555-3140
fax: (646) 555-2973
email: dkastrup@silvermerepartners.example
website: www.silvermerepartners.example

Target Market(s)

Business clients. Often real estate development firms, other advisory firms or growing companies that need assistance. I would like a card that looks impressive and confident.

Industry/Entity Type

Business

Colors

Designer to choose colors to be used in the design.

Requirements
Must have
• Impressive and confident. Please include logo.
Should not have
• nothing flashy...

```html
<!DOCTYPE html>
<html lang="en">
<head>
<meta charset="utf-8">
<title>Silvermere Advisory Partners — Business Card</title>
<link href="https://fonts.googleapis.com/css2?family=Lato:wght@400;700&display=swap" rel="stylesheet">
<style>
  :root {
    --lime: #a5c935;
    --lime-light: #b4d24a;
    --graphite: #55575a;
    --graphite-dark: #4d4e50;
    --band-grey: #7a7b7d;
    --paper: #fbfbfa;
    --backdrop: #e4e4e2;
  }
  * { margin: 0; padding: 0; box-sizing: border-box; }
  html, body {
    width: 1200px; height: 1000px; overflow: hidden;
    background: var(--backdrop);
    font-family: "Lato", sans-serif;
  }
  .sheet {
    position: relative; width: 1200px; height: 1000px;
    display: flex; flex-direction: column; align-items: center;
    justify-content: center; gap: 22px;
  }
  .card {
    position: relative; width: 820px; height: 469px; overflow: hidden;
    box-shadow: 0 6px 18px rgba(0,0,0,.12);
  }

  /* Front */
  .card--front { background: var(--lime); }
  .front-brand {
    position: absolute; left: 150px; top: 150px;
    display: flex; align-items: center; gap: 40px;
  }
  .brand-square {
    width: 140px; height: 140px; background: var(--graphite); flex: none;
  }
  .front-brand .brand-name {
    color: var(--graphite); font-weight: 700; font-size: 46px;
    line-height: 1.02; font-variant: small-caps; letter-spacing: .5px;
  }

  /* Back */
  .card--back { background: var(--paper); }
  .back-shapes { position: absolute; inset: 0; }
  .back-brand {
    position: absolute; left: 38px; top: 30px;
    display: flex; align-items: center; gap: 18px;
  }
  .back-brand .brand-square { width: 74px; height: 74px; }
  .back-brand .brand-name {
    color: var(--graphite); font-weight: 700; font-size: 22px;
    line-height: 1.05; font-variant: small-caps;
  }
  .person-name {
    position: absolute; right: 40px; top: 148px;
    color: var(--graphite); font-weight: 700; font-size: 28px;
  }
  .contact-list {
    position: absolute; left: 34px; top: 250px; list-style: none;
    color: var(--graphite-dark); font-size: 21px; line-height: 28px;
  }
  .contact-list li { display: flex; align-items: center; gap: 10px; white-space: nowrap; }
  .contact-list svg { width: 18px; height: 18px; flex: none; fill: var(--graphite-dark); }
  .website {
    position: absolute; left: 34px; top: 378px;
    color: var(--graphite-dark); font-size: 24px;
  }
  .website strong { font-weight: 700; }
</style>
</head>
<body>
<main class="sheet">

  <section class="card card--front" aria-label="Card front">
    <div class="front-brand">
      <div class="brand-square" aria-hidden="true"></div>
      <div class="brand-name">Silvermere<br>Advisory<br>Partners, Inc.</div>
    </div>
  </section>

  <section class="card card--back" aria-label="Card back">
    <svg class="back-shapes" viewBox="0 0 820 469" aria-hidden="true">
      <path d="M0,126 C300,160 600,230 820,246" fill="none" stroke="var(--band-grey)" stroke-width="16"/>
      <path d="M0,148 C300,182 600,252 820,268 L820,469 L0,469 Z" fill="var(--lime)"/>
      <rect x="0" y="424" width="820" height="45" fill="var(--graphite)"/>
    </svg>

    <div class="back-brand">
      <div class="brand-square" aria-hidden="true"></div>
      <div class="brand-name">Silvermere<br>Advisory<br>Partners, Inc.</div>
    </div>

    <p class="person-name">Danielle R. Kastrup</p>

    <ul class="contact-list">
      <li>
        <svg viewBox="0 0 24 24"><path d="M12 2a7 7 0 0 0-7 7c0 5 7 13 7 13s7-8 7-13a7 7 0 0 0-7-7zm0 9.5A2.5 2.5 0 1 1 12 6.5a2.5 2.5 0 0 1 0 5z"/></svg>
        Four Ashgrove Court, New York, NY 10087
      </li>
      <li>
        <svg viewBox="0 0 24 24"><path d="M6.6 10.8a15 15 0 0 0 6.6 6.6l2.2-2.2c.3-.3.7-.4 1-.2 1.1.4 2.3.6 3.6.6.6 0 1 .4 1 1V20c0 .6-.4 1-1 1A17 17 0 0 1 3 4c0-.6.4-1 1-1h3.5c.6 0 1 .4 1 1 0 1.3.2 2.5.6 3.6.1.3 0 .7-.2 1z"/></svg>
        (917) 555-3140
      </li>
      <li>
        <svg viewBox="0 0 24 24"><path d="M3 5h18v16H3zM6 8v3h12V8zm0 6v2h3v-2zm5 0v2h3v-2zm5 0v2h2v-2z"/></svg>
        (646) 555-2973
      </li>
      <li>
        <svg viewBox="0 0 24 24"><path d="M2 5h20v14H2zm2 2v.5l8 5 8-5V7zm0 3v7h16v-7l-8 5z"/></svg>
        dkastrup@silvermerepartners.example
      </li>
    </ul>

    <p class="website">www.<strong>silvermerepartners</strong>.example</p>
  </section>

</main>
</body>
</html>
```